Business Card Design REAL ESTATE SALES PLEASE DESIGN MY CARD 2COLOR CARD WITH RED AS THE DOMINANT

FERNHOLM REALTY
TorLPA Lic# 04738216
RAFAEL " RAFE " MORTON Tel 555 218-3396
TorLPA Lic# 02864057 Fax 555 218-3740
Email: rafe@rafemortonhomes.net Cell 555 902-4481
47530 WREN TERRACE KESTREL FALLS, CA 94312

RAFAEL " RAFE " MORTON
TEL: 555 218-3396 FAX 555 218-3740
Address: 47530 Wren Terrace Union City , CA
EMAIL ADDRESS: rafe@rafemortonhomes.net

```html
<!DOCTYPE html>
<html lang="en">
<head>
<meta charset="utf-8">
<title>Fernholm Realty – Rafael "Rafe" Morton</title>
<link href="https://fonts.googleapis.com/css2?family=Oswald:wght@400&display=swap" rel="stylesheet">
<style>
  :root {
    --card-white: #ffffff;
    --brand-black: #141213;
    --brand-red: #e8141b;
    --ink: #1a1a1a;
  }
  html, body {
    margin: 0;
    padding: 0;
    width: 1200px;
    height: 702px;
    overflow: hidden;
    background: var(--card-white);
  }
  .card {
    position: relative;
    width: 1200px;
    height: 702px;
    background: var(--card-white);
    overflow: hidden;
    font-family: "Oswald", "Arial Narrow", sans-serif;
    color: var(--ink);
  }
  .brand-arrow {
    position: absolute;
    left: 0;
    top: 0;
    width: 1200px;
    height: 702px;
  }
  .brand-name {
    position: absolute;
    left: 60px;
    top: 250px;
    margin: 0;
    font-family: "Oswald", "Arial Narrow", sans-serif;
    font-weight: 400;
    font-size: 84px;
    line-height: 1.1;
    letter-spacing: 4px;
    color: var(--card-white);
  }
  .brand-name span {
    display: block;
  }
  .agent-name {
    position: absolute;
    left: 668px;
    top: 76px;
    margin: 0;
    font-size: 48px;
    font-weight: 400;
    line-height: 1.2;
    letter-spacing: 0.5px;
    padding-bottom: 6px;
    border-bottom: 7px solid var(--brand-red);
    white-space: nowrap;
  }
  .contact-list {
    position: absolute;
    left: 691px;
    top: 304px;
    margin: 0;
    padding: 0;
    list-style: none;
  }
  .contact-item {
    display: flex;
    align-items: center;
    height: 82px;
    margin-bottom: 32px;
  }
  .contact-icon {
    flex: none;
    width: 72px;
    height: 72px;
    margin-right: 26px;
  }
  .contact-text {
    font-size: 34px;
    line-height: 1.3;
    white-space: nowrap;
  }
</style>
</head>
<body>
<div class="card">
  <svg class="brand-arrow" viewBox="0 0 1200 702" aria-hidden="true">
    <polygon points="0,-28 664,351 0,730" fill="var(--brand-red)"/>
    <polygon points="0,-10 632,351 0,712" fill="var(--brand-black)"/>
  </svg>

  <h2 class="brand-name">
    <span>FERNHOLM</span>
    <span>REALTY</span>
  </h2>

  <h1 class="agent-name">RAFAEL " RAFE " MORTON</h1>

  <ul class="contact-list">
    <li class="contact-item">
      <svg class="contact-icon" viewBox="0 0 72 72" aria-hidden="true">
        <rect width="72" height="72" rx="6" fill="var(--brand-red)"/>
        <rect x="14" y="14" width="44" height="44" rx="6" fill="none" stroke="#fff" stroke-width="3"/>
        <path d="M26 20c2-1 4 0 5 2l3 6c1 2 0 3-1 4l-2 2c2 4 5 7 9 9l2-2c1-1 2-2 4-1l6 3c2 1 3 3 2 5l-2 3c-2 2-5 3-8 2-10-4-18-12-22-22-1-3 0-6 2-8z" fill="#fff"/>
      </svg>
      <div class="contact-text">555 218-3396<br>Fax: 555 218-3740</div>
    </li>
    <li class="contact-item">
      <svg class="contact-icon" viewBox="0 0 72 72" aria-hidden="true">
        <rect width="72" height="72" rx="6" fill="var(--brand-red)"/>
        <rect x="10" y="18" width="52" height="36" fill="none" stroke="#fff" stroke-width="3"/>
        <polyline points="10,18 36,40 62,18" fill="none" stroke="#fff" stroke-width="3"/>
        <line x1="10" y1="54" x2="29" y2="35" stroke="#fff" stroke-width="3"/>
        <line x1="62" y1="54" x2="43" y2="35" stroke="#fff" stroke-width="3"/>
      </svg>
      <div class="contact-text">rafe@rafemortonhomes.net</div>
    </li>
    <li class="contact-item">
      <svg class="contact-icon" viewBox="0 0 72 72" aria-hidden="true">
        <rect width="72" height="72" rx="6" fill="var(--brand-red)"/>
        <g fill="none" stroke="#fff" stroke-width="3">
          <circle cx="36" cy="36" r="23"/>
          <ellipse cx="36" cy="36" rx="10" ry="23"/>
          <line x1="36" y1="13" x2="36" y2="59"/>
          <line x1="13" y1="36" x2="59" y2="36"/>
          <line x1="17" y1="25" x2="55" y2="25"/>
          <line x1="17" y1="47" x2="55" y2="47"/>
        </g>
      </svg>
      <div class="contact-text">47530 Wren Terrace.<br>Kestrel Falls, CA</div>
    </li>
  </ul>
</div>
</body>
</html>
```